Minimalist, Flat(Matte) design for a Beef Jerky packaging company. No bullshit company looking for a

Need a packaging design for a new Beef Jerky product(in English). The name of the company is 'Velmor' and thus the packaging should reflect the bullish, tough, and simple nature of the beef jerky product. The finished product should communicate simplicity, minimalism, yet toughness and strength.

The logo should be simple, with a minimal number of colors , and should be either all white/cream, or have some red as well. Main colors should be white, cream, tinted red, and matte black. I think 4 colors max would be best. The closest example to an existing package style would be Korvanti Dusk clove cigarettes( image attached).

It will be on a matte black standing pouch package. See image for package type. Package dimensions:

Dimension: Width x Gusset x Height
INCH : 5.125" (W) x 3.125" (G) x 8.125" (H)
MILLIMETER : 130mm (W) x 80mm (G) x 205mm (H)

I don't have anything totally specific so artistic liberty is encouraged, provided the colors are kept to a minimum and looks consistent with the simple nature of the brand and the matte black packaging.

Also attached an existing beef jerky package with a similar style to what we're looking for.

Industry/Entity Type

It Company

Colors
f59195
ffffff

Requirements
Must have
• Low contrast, flat and minimalist design.
Should not have
• A complicated design with many colors. Gawdy/flashy design. Bright colors. High contrast.

```html
<!DOCTYPE html>
<html lang="en">
<head>
<meta charset="utf-8">
<title>Velmor Hand Crafted Beef Jerky – Peppered Pouch Label</title>
<link rel="stylesheet" href="https://fonts.googleapis.com/css2?family=Poppins:wght@300;700&family=Josefin+Sans:wght@300&display=swap">
<style>
  :root {
    --backdrop: #ebe9e6;
    --pouch-black: #050505;
    --tint-red: #f59195;
    --white: #ffffff;
  }
  * { margin: 0; padding: 0; box-sizing: border-box; }
  html, body {
    width: 1200px;
    height: 612px;
    overflow: hidden;
    background: var(--backdrop);
  }
  .canvas {
    position: relative;
    width: 1200px;
    height: 612px;
    display: flex;
    align-items: center;
    justify-content: center;
  }
  .label {
    position: relative;
    width: 358px;
    height: 560px;
    background: var(--pouch-black);
    border: 1px solid var(--tint-red);
    color: var(--white);
  }
  .rule {
    position: absolute;
    left: 42px;
    right: 42px;
    height: 1px;
    background: var(--white);
  }
  .rule--top { top: 73px; height: 2px; }
  .rule--mid { top: 257px; }
  .brand {
    position: absolute;
    top: 90px;
    left: 0;
    right: 0;
    display: flex;
    flex-direction: column;
    align-items: center;
    gap: 16px;
  }
  .brand__name {
    font-family: "Poppins", sans-serif;
    font-weight: 700;
    font-size: 20px;
    letter-spacing: 0.02em;
    line-height: 1;
  }
  .brand__dot {
    width: 14px;
    height: 14px;
    border-radius: 50%;
    background: var(--tint-red);
  }
  .tagline {
    position: absolute;
    top: 223px;
    left: 0;
    right: 0;
    text-align: center;
    font-family: "Poppins", sans-serif;
    font-weight: 300;
    font-size: 27px;
    line-height: 1;
    letter-spacing: 0.01em;
  }
  .product {
    position: absolute;
    top: 278px;
    left: 0;
    right: 0;
    text-align: center;
    font-family: "Poppins", sans-serif;
    font-weight: 700;
    font-size: 31px;
    line-height: 1;
    letter-spacing: 0.06em;
  }
  .flavour {
    position: absolute;
    top: 394px;
    left: 0;
    right: 0;
    text-align: center;
    font-family: "Josefin Sans", sans-serif;
    font-weight: 300;
    font-size: 37px;
    line-height: 1;
    letter-spacing: 0.02em;
    color: var(--tint-red);
  }
  .net-weight {
    position: absolute;
    bottom: 26px;
    right: 34px;
    font-family: "Poppins", sans-serif;
    font-weight: 300;
    font-size: 13px;
    line-height: 1;
  }
</style>
</head>
<body>
  <main class="canvas">
    <section class="label">
      <div class="rule rule--top"></div>
      <div class="brand">
        <span class="brand__name">VELMOR</span>
        <span class="brand__dot"></span>
      </div>
      <p class="tagline">HAND CRAFTED</p>
      <div class="rule rule--mid"></div>
      <h1 class="product">BEEF JERKY</h1>
      <p class="flavour">PEPPERED</p>
      <p class="net-weight">3oz/100g</p>
    </section>
  </main>
</body>
</html>
```